Brightmark Electrical Flyer

An eye catching flyer design which showcases the type of work we do in the electrical industry in Vancouver,BC. The final design should be simple and incorporate our logo. And present a high end company.

Industry/Entity Type

Electrical

```html
<!DOCTYPE html>
<html lang="en">
<head>
<meta charset="utf-8">
<title>Brightmark Electrical Flyer</title>
<link rel="stylesheet" href="https://fonts.googleapis.com/css2?family=Orbitron:wght@900&family=Exo+2:wght@600;700;800&family=Oswald:wght@500&family=Open+Sans:wght@400;600&display=swap">
<style>
  :root {
    --yellow: #f7d417;
    --yellow-deep: #eab800;
    --ink: #1d1d1f;
    --charcoal: #3a3a3c;
    --frame: #4a4a4c;
    --paper: #ffffff;
    --mist: #ececec;
    --steel: #5d7a93;
    --steel-light: #b9cad8;
    --backdrop: #e4e4e4;
  }
  * { margin: 0; padding: 0; box-sizing: border-box; }
  html, body { width: 1200px; height: 1200px; overflow: hidden; }
  body {
    background: var(--backdrop);
    font-family: "Open Sans", sans-serif;
    color: var(--ink);
    position: relative;
  }
  .flyer {
    position: absolute;
    left: 210px; top: 50px;
    width: 780px; height: 1100px;
    background: linear-gradient(180deg, var(--paper) 60%, var(--mist) 100%);
    overflow: hidden;
    box-shadow: 0 10px 30px rgba(0,0,0,.18);
  }
  .hero-photo {
    position: absolute; left: 0; top: 0; width: 780px; height: 400px;
    background: linear-gradient(200deg, #ffffff 0%, #f3f6f9 22%, var(--steel-light) 45%, var(--steel) 75%, #2f4558 100%);
  }
  .brand {
    position: absolute; right: 50px; top: 95px;
    display: flex; align-items: center; gap: 12px;
    font-family: "Exo 2", sans-serif; font-weight: 800;
    font-size: 40px; color: var(--charcoal); letter-spacing: 1px;
  }
  .brand-dot { width: 22px; height: 22px; border-radius: 50%; background: var(--yellow); }
  .hero-divider { position: absolute; left: 0; top: 400px; width: 780px; height: 8px; background: var(--paper); border-bottom: 4px solid var(--ink); }
  .yellow-band {
    position: absolute; left: 0; top: 412px; width: 780px; height: 330px;
    background: linear-gradient(160deg, var(--yellow) 0%, #ffe04a 50%, var(--yellow-deep) 100%);
    clip-path: polygon(0 0, 100% 0, 100% 100%, 0 88%);
  }
  .headline {
    position: absolute; left: 28px; top: 425px;
    font-family: "Orbitron", sans-serif; font-weight: 900;
    line-height: .95; font-size: 76px; transform: skewX(-8deg);
  }
  .headline .line-dark { color: var(--ink); display: block; }
  .headline .line-light { color: var(--paper); display: block; -webkit-text-stroke: 3px var(--ink); }
  .tagline {
    position: absolute; left: 28px; top: 578px;
    font-family: "Oswald", sans-serif; font-weight: 500; font-size: 19px; line-height: 1.2;
    color: var(--ink); white-space: nowrap;
  }
  .services-tab {
    position: absolute; right: 0; top: 432px; width: 330px; height: 58px;
    background: var(--ink);
    clip-path: polygon(12% 0, 100% 0, 100% 100%, 0 100%);
    font-family: "Exo 2", sans-serif; font-weight: 800; font-size: 30px; color: var(--paper);
    display: flex; align-items: center; padding-left: 60px;
  }
  .services-list {
    position: absolute; right: 28px; top: 500px; list-style: none; text-align: right;
    font-family: "Exo 2", sans-serif; font-weight: 600; font-size: 22px; color: var(--ink); line-height: 1.2;
  }
  .services-list li { display: flex; justify-content: flex-end; align-items: center; gap: 8px; }
  .services-list svg { width: 16px; height: 16px; }
  .photo-frame { position: absolute; border: 8px solid var(--frame); box-shadow: 0 6px 12px rgba(0,0,0,.25); }
  .photo-lighting { left: 34px; top: 632px; width: 200px; height: 140px; background: linear-gradient(135deg, #5a2a12, #e7751c 50%, #ffd04a); }
  .photo-panel { left: 250px; top: 618px; width: 270px; height: 186px; background: linear-gradient(90deg, #f1ede2 0%, #e9e4d8 30%, #2d3440 45%, #1d2430 65%, #8c9098 100%); }
  .photo-worker { left: 538px; top: 676px; width: 210px; height: 150px; background: linear-gradient(135deg, #a85a3c, #d8c2a4 45%, #f2c21a 60%, #6b4a2e); }
  .caption { position: absolute; text-align: center; }
  .caption h3 { font-family: "Oswald", sans-serif; font-weight: 500; font-size: 19px; line-height: 1.25; color: var(--ink); white-space: nowrap; }
  .caption p { font-size: 11px; line-height: 1.35; color: var(--charcoal); margin-top: 4px; }
  .cap-lighting { left: 34px; top: 784px; width: 200px; }
  .cap-panel { left: 250px; top: 814px; width: 270px; }
  .cap-quality { left: 523px; top: 836px; width: 240px; }
  .about { position: absolute; left: 40px; top: 876px; width: 300px; }
  .about h2 { font-family: "Exo 2", sans-serif; font-weight: 800; font-size: 24px; line-height: 1.2; }
  .about p { font-size: 13px; line-height: 1.4; color: var(--charcoal); margin-top: 6px; }
  .contact {
    position: absolute; left: 370px; top: 930px; width: 380px; height: 82px;
    background: var(--yellow); border-right: 8px solid var(--ink);
    clip-path: polygon(0 0, 100% 0, 100% 100%, 6% 100%);
    padding: 12px 0 0 40px;
    font-family: "Oswald", sans-serif; font-weight: 500; color: var(--ink);
    white-space: nowrap;
  }
  .contact .phone { font-size: 24px; line-height: 1.15; }
  .contact .mail { font-size: 15px; line-height: 1.2; margin-top: 6px; }
  .contact-edge { position: absolute; left: 355px; top: 930px; width: 30px; height: 82px; background: var(--ink); clip-path: polygon(0 0, 50% 0, 100% 100%, 50% 100%); }
  .footer { position: absolute; left: 0; bottom: 0; width: 780px; height: 76px; background: var(--ink); }
  .footer-invite {
    position: absolute; left: 0; top: 0; width: 440px; height: 76px; background: var(--yellow);
    clip-path: polygon(0 0, 88% 0, 100% 100%, 0 100%);
    font-family: "Exo 2", sans-serif; font-weight: 600; font-size: 20px;
    display: flex; align-items: center; padding-left: 40px;
  }
  .footer-web {
    position: absolute; right: 40px; top: 0; height: 76px; display: flex; align-items: center;
    font-family: "Exo 2", sans-serif; font-weight: 600; font-size: 21px; color: var(--paper);
  }
</style>
</head>
<body>
  <div class="flyer">
    <div class="hero-photo" role="img" aria-label="Photo of modern glass office towers against a bright sky"></div>
    <div class="brand"><span class="brand-dot"></span>Brightmark Electrical</div>
    <div class="hero-divider"></div>

    <div class="yellow-band"></div>
    <h1 class="headline"><span class="line-dark">BUILDING</span><span class="line-light">DREAMS</span></h1>
    <p class="tagline">EXPERT DESIGNERS TURN YOUR DREAMS INTO REALITY</p>

    <div class="services-tab">Our Services:</div>
    <ul class="services-list">
      <li>Fire Alarm <svg viewBox="0 0 16 16"><circle cx="8" cy="8" r="6.5" fill="none" stroke="#1d1d1f" stroke-width="1.5"/><path d="M10.5 5v6L5 8z" fill="#1d1d1f"/></svg></li>
      <li>Security Service <svg viewBox="0 0 16 16"><circle cx="8" cy="8" r="6.5" fill="none" stroke="#1d1d1f" stroke-width="1.5"/><path d="M10.5 5v6L5 8z" fill="#1d1d1f"/></svg></li>
      <li>Solar Panel <svg viewBox="0 0 16 16"><circle cx="8" cy="8" r="6.5" fill="none" stroke="#1d1d1f" stroke-width="1.5"/><path d="M10.5 5v6L5 8z" fill="#1d1d1f"/></svg></li>
      <li>Residential lighting <svg viewBox="0 0 16 16"><circle cx="8" cy="8" r="6.5" fill="none" stroke="#1d1d1f" stroke-width="1.5"/><path d="M10.5 5v6L5 8z" fill="#1d1d1f"/></svg></li>
      <li>Commerical lighting <svg viewBox="0 0 16 16"><circle cx="8" cy="8" r="6.5" fill="none" stroke="#1d1d1f" stroke-width="1.5"/><path d="M10.5 5v6L5 8z" fill="#1d1d1f"/></svg></li>
      <li>Low Voltage Wiring <svg viewBox="0 0 16 16"><circle cx="8" cy="8" r="6.5" fill="none" stroke="#1d1d1f" stroke-width="1.5"/><path d="M10.5 5v6L5 8z" fill="#1d1d1f"/></svg></li>
    </ul>

    <div class="photo-frame photo-lighting" role="img" aria-label="Photo of a warmly lit corridor with decorative wall lighting"></div>
    <div class="photo-frame photo-panel" role="img" aria-label="Photo of an open electrical smart lighting panel"></div>
    <div class="photo-frame photo-worker" role="img" aria-label="Photo of an electrician holding a yellow hard hat and tool belt"></div>

    <div class="caption cap-lighting">
      <h3>LIGHTING EXPERTS</h3>
      <p>We provide all your lighting needs to complete any project from small to large.</p>
    </div>
    <div class="caption cap-panel">
      <h3>PANELIZED SMART LIGHTING</h3>
      <p>Smart lighting solutions give you endless options with your lights</p>
    </div>
    <div class="caption cap-quality">
      <h3>QUALITY ON TIME CONSTRUCTION</h3>
      <p>We efficiently manage construction and coordinate with schedules to always give our clients an effortless experience.</p>
    </div>

    <div class="about">
      <h2>ABOUT US</h2>
      <p>We are an electrical contractor serving the lower mainland. Providing the best in customer service and knowledge, to our clients.</p>
    </div>

    <div class="contact-edge"></div>
    <div class="contact">
      <div class="phone">CONTACT US AT: 604 555 0148</div>
      <div class="mail">MAIL US: INFO@BRIGHTMARKELECTRICAL.CA</div>
    </div>

    <div class="footer">
      <div class="footer-invite">Join us now for more informations:</div>
      <div class="footer-web">www.brightmarkelectrical.ca</div>
    </div>
  </div>
</body>
</html>
```